Rural Water and Sewer District No. 14, McClain County, Oklahoma

This will be for our public utilities' corporation; this is for our first board meeting.

Special Meeting of landowners to select the board of directors. and adopt bylaws for the district.

Target Market(s)

Our property owners

Industry/Entity Type

Utilities

Requirements
Must have
• This is a green project. We believe in water resuse and environmentally friendly solutions.
Should not have
• Prioritizing climate-smart, energy efficient infrastructure to ensure our communities are safe, healthy, and sustainable

```html
<!DOCTYPE html>
<html lang="en">
<head>
<meta charset="utf-8">
<title>Rural Water and Sewer District No. 14 — Special Meeting Flyer</title>
<link rel="stylesheet" href="https://fonts.googleapis.com/css2?family=Montserrat:wght@400;500;700&family=Oswald:wght@500;600&display=swap">
<style>
  :root {
    --backdrop: #ebebeb;
    --navy: #2f4f7f;
    --band-blue: #4a72a3;
    --cream: #e8e6da;
    --lime: #b5cf6a;
    --leaf: #8aab55;
    --leaf-deep: #7f9f4c;
    --white: #ffffff;
    --photo-light: #d9dde3;
    --photo-skin: #c39a80;
    --photo-navy: #3b4a6b;
  }
  * { margin: 0; padding: 0; box-sizing: border-box; }
  html, body {
    width: 1200px;
    height: 800px;
    overflow: hidden;
    background: var(--backdrop);
  }
  .canvas {
    position: relative;
    width: 1200px;
    height: 800px;
  }
  .flyer {
    position: absolute;
    left: 330px;
    top: 20px;
    width: 540px;
    height: 760px;
    box-shadow: 0 6px 24px rgba(0,0,0,0.12);
  }
  .flyer svg { display: block; }
  .title { font-family: "Oswald", sans-serif; font-weight: 600; }
  .pill-text { font-family: "Oswald", sans-serif; font-weight: 500; }
  .body-text { font-family: "Montserrat", sans-serif; }
</style>
</head>
<body>
<main class="canvas">
  <article class="flyer">
    <svg width="540" height="760" viewBox="0 0 540 760">
      <defs>
        <linearGradient id="photo-tones" x1="0" y1="1" x2="1" y2="0">
          <stop offset="0" stop-color="var(--photo-navy)"/>
          <stop offset="0.35" stop-color="var(--photo-skin)"/>
          <stop offset="0.7" stop-color="#d4b79f"/>
          <stop offset="1" stop-color="var(--photo-light)"/>
        </linearGradient>
      </defs>

      <!-- Hero photo area -->
      <rect class="hero-photo" x="0" y="0" width="540" height="480" fill="url(#photo-tones)" role="img" aria-label="Photo of several hands clasped together in a circle, symbolising community teamwork"/>

      <!-- Layered curved bands -->
      <path class="band-blue" d="M0,600 Q250,330 540,300 L540,760 L0,760 Z" fill="var(--band-blue)"/>
      <path class="band-cream" d="M0,622 Q262,362 540,334 L540,760 L0,760 Z" fill="var(--cream)"/>
      <path class="band-lime" d="M0,640 Q272,384 540,350 L540,760 L0,760 Z" fill="var(--lime)"/>
      <path class="panel-green" d="M0,680 Q292,424 540,396 L540,760 L0,760 Z" fill="var(--leaf)"/>

      <!-- Inset frame -->
      <rect class="frame" x="16" y="16" width="508" height="728" fill="none" stroke="var(--cream)" stroke-width="1.5"/>

      <!-- District badge -->
      <g class="badge">
        <circle cx="185" cy="445" r="100" fill="var(--cream)"/>
        <circle cx="185" cy="445" r="86" fill="var(--lime)"/>
        <text class="body-text" x="185" y="440" text-anchor="middle" font-size="22" font-weight="700" fill="var(--navy)">District</text>
        <text class="body-text" x="185" y="468" text-anchor="middle" font-size="22" font-weight="700" fill="var(--navy)">No. 14</text>
      </g>

      <!-- Meeting details box -->
      <g class="details">
        <rect x="305" y="385" width="200" height="138" rx="18" fill="none" stroke="var(--lime)" stroke-width="1.5"/>
        <text class="body-text" x="405" y="423" text-anchor="middle" font-size="14" font-weight="500" fill="var(--white)">Add Date</text>
        <text class="body-text" x="405" y="447" text-anchor="middle" font-size="14" font-weight="500" fill="var(--white)">Add Time</text>
        <text class="body-text" x="405" y="471" text-anchor="middle" font-size="14" font-weight="500" fill="var(--white)">Add Place</text>
        <text class="body-text" x="405" y="495" text-anchor="middle" font-size="14" font-weight="500" fill="var(--white)">Add Contact Details</text>
      </g>

      <!-- Title block -->
      <text class="title" x="40" y="578" font-size="40" fill="var(--white)" letter-spacing="0.5">RURAL WATER AND SEWER</text>
      <rect class="district-pill" x="200" y="594" width="310" height="46" rx="23" fill="var(--band-blue)"/>
      <text class="pill-text" x="355" y="628" text-anchor="middle" font-size="28" fill="var(--white)" letter-spacing="1">DISTRICT NO. 14</text>
      <text class="body-text" x="505" y="686" text-anchor="end" font-size="36" font-weight="500" fill="var(--white)">McClain County</text>
      <text class="body-text" x="505" y="722" text-anchor="end" font-size="30" font-weight="500" fill="var(--lime)" letter-spacing="1">OKLAHOMA</text>
      <line class="rule" x1="170" y1="734" x2="510" y2="734" stroke="var(--lime)" stroke-width="1.5"/>
    </svg>
  </article>
</main>
</body>
</html>
```